Psychotherapist's business card

I need a business card design for a psychotherapist. I expect business card to have "light" design. By this I mean that it can somehow translate easiness, serenity. Maybe pastel colours can help you here. I have attached some pictures from Greece. Perhaps they can inspire you to combine colours and to achieve that "light" design.
Updates

Pls, don't use any free samples you may find on business card generators. It looks too simple, uncreative and waste of time! READ size and colour requirements! I don't want to see any shapes like rings, triangles etc.

Contact Information for Business Card

Size: 65mmX60mm

Name - Вячеслав Мирошенко

Психолог
+7(916)482-30-67
miroshenko.com

I suppose that thin font can look good but it's up to you

Requirements
Must have
• size requirements
Nice to have
• pastel colours
• thin font
Should not have
• black and dark colours
• lines, free design samples used from other web-sites

```html
<!DOCTYPE html>
<html lang="en">
<head>
<meta charset="utf-8">
<title>Psychologist – Business Card</title>
<link rel="stylesheet" href="https://fonts.googleapis.com/css2?family=Poiret+One&family=Questrial&display=swap">
<style>
  :root {
    --backdrop: #000000;
    --card-white: #ffffff;
    --sea-blue: #1791cf;
    --mint: #88d1c7;
    --text-blue: #1f86c8;
    --sky-light: #86c9ea;
  }
  html, body {
    margin: 0;
    width: 1200px;
    height: 999px;
    overflow: hidden;
    background: var(--backdrop);
  }
  .business-card {
    position: absolute;
    left: 216px;
    top: 145px;
    width: 768px;
    height: 708px;
    background: var(--card-white);
    overflow: hidden;
  }
  .header-field {
    position: absolute;
    inset: 0;
    width: 768px;
    height: 708px;
  }
  .header-field .blue-field { fill: var(--sea-blue); }
  .header-field .mint-edge { fill: var(--mint); }
  .card-title {
    position: absolute;
    left: 0;
    right: 0;
    top: 42px;
    margin: 0;
    text-align: center;
    font-family: "Poiret One", sans-serif;
    font-weight: 400;
    font-size: 94px;
    line-height: 1;
    letter-spacing: 2px;
    color: var(--card-white);
    transform: translateX(9px);
  }
  .contact {
    position: absolute;
    left: 43px;
    top: 0;
    margin: 0;
    font-family: "Questrial", sans-serif;
    color: var(--text-blue);
    font-style: normal;
  }
  .contact > * {
    position: absolute;
    left: 0;
    margin: 0;
    white-space: nowrap;
    line-height: 1;
  }
  .contact .person-name { top: 503px; font-size: 32px; font-weight: 400; }
  .contact .phone { top: 578px; font-size: 28px; }
  .contact .email { top: 635px; font-size: 28px; }
  .tree-emblem {
    position: absolute;
    left: 474px;
    top: 403px;
    width: 262px;
    height: 305px;
    border-radius: 131px 131px 0 0;
    background:
      radial-gradient(circle at 50% 32%, rgba(134, 201, 234, 0.85), rgba(136, 209, 199, 0.6) 45%, rgba(255, 255, 255, 0) 70%),
      linear-gradient(to bottom, rgba(255,255,255,0) 55%, rgba(23, 145, 207, 0.35) 100%);
  }
</style>
</head>
<body>
  <section class="business-card">
    <svg class="header-field" viewBox="0 0 768 708" aria-hidden="true">
      <path class="mint-edge" d="M0,300 C220,380 420,250 768,330 V300 C420,230 220,350 0,280 Z"/>
      <path class="blue-field" d="M0,0 H768 V290 C420,220 220,340 0,262 Z"/>
    </svg>

    <h1 class="card-title">Psychologist</h1>

    <address class="contact">
      <h2 class="person-name">Vyacheslav Miroshenko</h2>
      <p class="phone">Ph: +7(916)482-30-67</p>
      <p class="email">Email: miroshenko.com</p>
    </address>

    <div class="tree-emblem" role="img" aria-label="Tree illustration: a stylised figure with raised arms forming a trunk, crowned by translucent blue and mint circles"></div>
  </section>
</body>
</html>
```